KESTRA BLOOMS (Gummie)

TASK IDEA Only: I want a gummy bear like (Icon) flexing his muscles as the logo on the label.

What I upload is not mine and is only for demonstration purposes. You can create your own version or you may have a different idea or theme.

Purpose: these kestra blooms are "Post Workout Treats" and are infused with CBD, CBG & Delta-8.

Symbols to add

Hemp Leaf, Vegan, Non-GMO, Sugar Free, and Organic

I think the (90) gummies need to be in a clear 8-10 oz jar with a black lid. The label needs to allow some of the gummies to be seen a bit at the botttom of the jar because the gummies will come in two colors.

```html
<!DOCTYPE html>
<html lang="en">
<head>
<meta charset="utf-8">
<title>Kestra Blooms – Post Workout Treats label</title>
<link rel="stylesheet" href="https://fonts.googleapis.com/css2?family=Montserrat:wght@600;800;900&family=Open+Sans:wght@500;600&display=swap">
<style>
  :root {
    --page: #ffffff;
    --label-top: #2a3550;
    --label-mid: #141a28;
    --label-bottom: #0a0d14;
    --tab: #0b0d12;
    --gold: #c9a24f;
    --white: #ffffff;
    --sky: #4aa6ea;
    --bear-red: #d8231c;
    --bear-dark: #8c0f0b;
    --logo-box: #0c0d10;
  }
  * { margin: 0; padding: 0; box-sizing: border-box; }
  html, body {
    width: 1200px; height: 942px; overflow: hidden;
    background: var(--page);
  }
  .label {
    position: absolute; left: 110px; top: 71px;
    width: 980px; height: 800px;
    background: linear-gradient(180deg, var(--label-top) 0%, var(--label-mid) 45%, var(--label-bottom) 100%);
    overflow: hidden;
  }
  .count-tab { position: absolute; left: 30px; top: 0; width: 150px; height: 200px; }
  .count-tab__text {
    position: absolute; left: 0; top: 38px; width: 100%;
    text-align: center; color: var(--white);
    font-family: "Montserrat", sans-serif;
  }
  .count-tab__number { display: block; font-size: 54px; font-weight: 800; line-height: 1; }
  .count-tab__unit {
    display: block; margin-top: 8px; font-size: 20px; font-weight: 600;
    letter-spacing: 2px; color: var(--gold);
  }
  .badge {
    position: absolute; left: 62px; width: 76px; height: 76px;
    border: 3px solid var(--gold); border-radius: 50%;
  }
  .bear-art {
    position: absolute; left: 340px; top: 90px; width: 260px; height: 230px;
    background: radial-gradient(ellipse at 50% 45%, var(--bear-red) 0%, var(--bear-red) 45%, var(--bear-dark) 100%);
    border-radius: 40% 40% 20% 20%;
  }
  .logo-box {
    position: absolute; left: 200px; top: 304px; width: 570px; height: 246px;
    background: var(--logo-box); border-radius: 22px;
    display: flex; flex-direction: column; align-items: center; justify-content: center;
  }
  .logo-box__name {
    font-family: "Montserrat", sans-serif; font-weight: 900;
    font-size: 96px; line-height: 0.98; color: var(--white);
    text-align: center; letter-spacing: 1px;
  }
  .rule {
    position: absolute; left: 200px; top: 558px; width: 570px; height: 3px;
    background: var(--gold);
  }
  .tagline {
    position: absolute; left: 0; top: 578px; width: 970px; text-align: center;
    font-family: "Montserrat", sans-serif; font-weight: 800;
    font-size: 50px; color: var(--sky);
  }
  .infusion {
    position: absolute; left: 0; top: 695px; width: 970px; text-align: center;
    font-family: "Open Sans", sans-serif; font-weight: 600;
    font-size: 27px; line-height: 46px; letter-spacing: 1.5px; color: var(--white);
  }
  .infusion__compound { color: var(--gold); }
</style>
</head>
<body>
  <main class="label">
    <div class="count-tab">
      <svg width="150" height="200" viewBox="0 0 150 200" aria-hidden="true">
        <polygon points="0,0 150,0 150,200 75,168 0,200" fill="var(--tab)"/>
      </svg>
      <div class="count-tab__text">
        <span class="count-tab__number">90</span>
        <span class="count-tab__unit">GUMMIES</span>
      </div>
    </div>

    <div class="badge" style="top:256px" role="img" aria-label="Hemp leaf symbol"></div>
    <div class="badge" style="top:356px" role="img" aria-label="Vegan symbol"></div>
    <div class="badge" style="top:470px" role="img" aria-label="Non-GMO symbol"></div>
    <div class="badge" style="top:580px" role="img" aria-label="Sugar free symbol"></div>
    <div class="badge" style="top:696px" role="img" aria-label="Organic symbol"></div>

    <div class="bear-art" role="img" aria-label="Red gummy bear flexing its muscles"></div>

    <div class="logo-box">
      <div class="logo-box__name">KESTRA<br>BLOOMS</div>
    </div>
    <div class="rule"></div>

    <p class="tagline">Post Workout Treats</p>

    <p class="infusion">GUMMIES INFUSED<br>WITH <span class="infusion__compound">CBD</span>, <span class="infusion__compound">CBG</span> &amp; <span class="infusion__compound">DELTA-8</span>.</p>
  </main>
</body>
</html>
```